Electronic Music Artist needs an Album Cover

DRELL is an electronic musician from Boston, Massachusetts. He needs an album cover that captures the essence of his music. The album is called Waypoints, which represents his experiences growing up, positive and negative. He would like to see designs that involves color and creativity. Attached are some examples of artworks that DRELL likes. He also included a few of his original photos (optional to use. Using a photo will not effect his final decision!), and his logo.
Updates

Colors

Designer to choose colors to be used in the design.

Requirements
Must have
• My project must have the text "Waypoints" and "DRELL", and the logo (attached in the files). The logo should not be the main subject of the artwork. Everything must look aesthetically pleasing.
Nice to have
• It would be nice to have some sort of creative graphic design (see example album covers for reference). Also, in one of the references, there is a column on the left hand side with some text in it. That could be cool to include, but without the asian text.
Should not have
• The project should not have any other language besides English.

```html
<!DOCTYPE html>
<html lang="en">
<head>
<meta charset="utf-8">
<title>DRELL — Waypoints album cover</title>
<link rel="stylesheet" href="https://fonts.googleapis.com/css2?family=Josefin+Sans:wght@300&display=swap">
<style>
  :root {
    --page: #ffffff;
    --ink-light: #ffffff;
    --ink-grey: #8c8c8c;
    --warm-clay: #c27c5c;
    --warm-rose: #cf7b74;
    --warm-cream: #eee2d2;
    --warm-sage: #98c58c;
    --grass-gold: #8a7a55;
    --grass-deep: #1e2a1e;
    --sky-pale: #e6f0f4;
    --sky-white: #f7f8f8;
    --field-tan: #9a8660;
    --cool-blue: #2e9de8;
    --cool-cyan: #38e4e6;
    --cool-violet: #c070e6;
    --cool-teal: #1f6a5a;
  }
  * { margin: 0; padding: 0; box-sizing: border-box; }
  html, body { width: 1200px; height: 990px; overflow: hidden; background: var(--page); }
  .sheet { position: relative; width: 1200px; height: 990px; }
  .cover { position: absolute; overflow: hidden; }
  .cover-main { left: 33px; top: 120px; width: 741px; height: 742px; }
  .cover-daylight { left: 802px; top: 118px; width: 358px; height: 360px; }
  .cover-neon { left: 802px; top: 502px; width: 358px; height: 360px; }
  .cover-photo { position: absolute; inset: 0; }
  .cover-main .cover-photo {
    background:
      linear-gradient(to bottom, transparent 45%, rgba(120,105,70,0.85) 70%, var(--grass-deep) 100%),
      radial-gradient(ellipse 45% 40% at 12% 50%, var(--warm-rose), transparent 70%),
      linear-gradient(to right, var(--warm-clay) 0%, var(--warm-clay) 25%, var(--warm-cream) 50%, var(--warm-sage) 100%);
  }
  .cover-daylight .cover-photo {
    background:
      linear-gradient(to bottom, var(--sky-white) 0%, var(--sky-pale) 40%, var(--field-tan) 62%, #4a4a30 82%, var(--grass-deep) 100%);
  }
  .cover-neon .cover-photo {
    background:
      linear-gradient(to bottom, transparent 45%, rgba(30,110,100,0.8) 68%, #13261c 100%),
      radial-gradient(ellipse 35% 35% at 8% 45%, var(--cool-cyan), transparent 75%),
      linear-gradient(to right, var(--cool-blue) 0%, #8ec8f0 50%, var(--cool-violet) 100%);
  }
  .cover-type { position: absolute; inset: 0; width: 100%; height: 100%; }
  .artist-name, .album-title {
    font-family: "Josefin Sans", sans-serif;
    font-weight: 300;
  }
  .ink-light { fill: var(--ink-light); }
  .ink-grey { fill: var(--ink-grey); }
</style>
</head>
<body>
<main class="sheet">

  <section class="cover cover-main">
    <div class="cover-photo" role="img" aria-label="Photo of a figure walking through tall grass under a warm orange-to-green sky"></div>
    <svg class="cover-type" viewBox="0 0 741 742">
      <defs>
        <radialGradient id="sun-glow-main">
          <stop offset="0.7" stop-color="#ffffff"/>
          <stop offset="1" stop-color="#ffffff" stop-opacity="0"/>
        </radialGradient>
      </defs>
      <circle cx="636" cy="94" r="48" fill="url(#sun-glow-main)"/>
      <text class="artist-name ink-light" x="179" y="204" font-size="140" textLength="380" lengthAdjust="spacingAndGlyphs">DRELL</text>
      <text class="album-title ink-light" x="179" y="682" font-size="80" textLength="384" lengthAdjust="spacingAndGlyphs">WAYPOINTS</text>
    </svg>
  </section>

  <section class="cover cover-daylight">
    <div class="cover-photo" role="img" aria-label="Photo of a figure walking through tall grass under a pale sky"></div>
    <svg class="cover-type" viewBox="0 0 358 360">
      <text class="artist-name ink-grey" x="86" y="98" font-size="66" textLength="184" lengthAdjust="spacingAndGlyphs">DRELL</text>
      <text class="album-title ink-light" x="86" y="334" font-size="40" textLength="186" lengthAdjust="spacingAndGlyphs">WAYPOINTS</text>
    </svg>
  </section>

  <section class="cover cover-neon">
    <div class="cover-photo" role="img" aria-label="Photo of a figure walking through tall grass under a blue, cyan and violet sky"></div>
    <svg class="cover-type" viewBox="0 0 358 360">
      <defs>
        <radialGradient id="sun-glow-neon">
          <stop offset="0.65" stop-color="#ffffff"/>
          <stop offset="1" stop-color="#ffffff" stop-opacity="0"/>
        </radialGradient>
      </defs>
      <circle cx="308" cy="45" r="24" fill="url(#sun-glow-neon)"/>
      <text class="artist-name ink-light" x="86" y="98" font-size="66" textLength="184" lengthAdjust="spacingAndGlyphs">DRELL</text>
      <text class="album-title ink-light" x="86" y="334" font-size="40" textLength="186" lengthAdjust="spacingAndGlyphs">WAYPOINTS</text>
    </svg>
  </section>

</main>
</body>
</html>
```